Rin3Vox Header

I want a professional Letterhead for my law firm. I'm attaching the letterhead I currently use in Word and PDF form. I'm also attaching my logo, and an example header that I like.

```html
<!DOCTYPE html>
<html lang="en">
<head>
<meta charset="utf-8">
<title>Rin3Vox Stationery</title>
<link rel="stylesheet" href="https://fonts.googleapis.com/css2?family=Alegreya+Sans:ital,wght@0,400;0,500;0,800;1,400;1,500&family=Alegreya+Sans+SC:wght@400;500&display=swap">
<style>
:root{
  --canvas:#efe6cf;
  --paper:#ffffff;
  --card:#f1f1f1;
  --ink:#111111;
  --text:#4a4a4a;
  --muted:#666666;
  --teal:#2ba6c4;
  --green:#3f8a2c;
}
*{margin:0;padding:0;box-sizing:border-box}
html,body{width:1200px;height:1200px;overflow:hidden;background:var(--canvas)}
body{position:relative;font-family:"Alegreya Sans",sans-serif;color:var(--text)}
.letterhead{position:absolute;left:29px;top:118px;width:673px;height:936px;background:var(--paper);box-shadow:0 2px 8px rgba(0,0,0,.18)}
.abs{position:absolute}
.wordmark{font-family:"Alegreya Sans",sans-serif;font-weight:800;color:var(--ink);line-height:1;letter-spacing:-1px}
.tagline{font-family:"Alegreya Sans",sans-serif;font-weight:800;color:var(--ink);letter-spacing:5px;line-height:1;white-space:nowrap}
.address{right:42px;top:72px;text-align:right;font-style:italic;font-size:10.5px;line-height:13px;color:var(--muted);text-transform:uppercase}
.contact-bar{background:var(--teal);border-top:4px solid var(--green);display:flex;flex-direction:column;align-items:center;justify-content:space-around;padding:2px 0}
.contact-lines{font-style:italic;color:var(--muted);text-transform:uppercase}
.date{left:0;width:673px;top:212px;text-align:center;font-family:"Alegreya Sans SC",sans-serif;font-size:17px;color:var(--muted)}
.meta{font-family:"Alegreya Sans SC",sans-serif;font-size:10px;line-height:12.5px;color:var(--ink)}
.salutation{left:0;width:681px;top:366px;text-align:center;font-family:"Alegreya Sans SC",sans-serif;font-size:20px;color:var(--muted)}
.body-copy{left:46px;top:400px;width:588px;font-family:"Alegreya Sans SC",sans-serif;font-size:13.6px;line-height:17.5px;letter-spacing:.2px;color:var(--muted);text-align:justify}
.body-copy p{text-indent:32px}
.body-copy .gap{margin-top:17.5px}
.closing{left:63px;top:840px;font-family:"Alegreya Sans SC",sans-serif;font-size:15px;line-height:20px;color:var(--muted)}
.signature{left:245px;top:826px;width:160px;height:88px;background:linear-gradient(120deg,rgba(58,98,201,.05),rgba(58,98,201,.18),rgba(58,98,201,.05));border-radius:4px}
.card{position:absolute;width:411px;height:230px;background:var(--card);box-shadow:0 2px 8px rgba(0,0,0,.18)}
.card-front{left:739px;top:150px}
.card-back{left:739px;top:425px}
.site{left:0;width:411px;top:208px;text-align:center;font-style:italic;font-size:10px;color:var(--muted);text-transform:uppercase}
.site svg{vertical-align:-1px;margin-right:3px}
.card-name{right:20px;top:100px;font-style:italic;font-weight:500;font-size:20px;color:var(--ink);text-transform:uppercase}
.card-title{right:22px;top:134px;font-style:italic;font-size:13px;color:var(--teal);text-transform:uppercase}
</style>
</head>
<body>

<section class="letterhead">
  <div class="abs wordmark" style="left:44px;top:80px;font-size:66px;">Rin3Vox</div>
  <div class="abs tagline" style="left:70px;top:150px;font-size:9px;">COUNSEL &amp; ADVOCACY</div>

  <div class="abs address">Teodoro K. Almaden III, Attorney at Law, PLLC 2240<br>Larkspur Avenue Suite 300<br>Austin, Texas 78701</div>

  <div class="abs contact-bar" style="left:513px;top:114px;width:22px;height:56px;">
    <svg width="11" height="9" viewBox="0 0 11 9"><rect x=".5" y=".5" width="10" height="8" fill="none" stroke="#fff"/><path d="M.5 .5 5.5 5 10.5 .5" fill="none" stroke="#fff"/></svg>
    <svg width="10" height="10" viewBox="0 0 10 10"><path d="M2 1 4 3 3 4.5Q4.5 6.5 5.5 7L7 6 9 8 7.5 9.5Q3 8.5.5 2.5Z" fill="#fff"/></svg>
    <svg width="10" height="11" viewBox="0 0 10 11"><rect x=".5" y="3" width="9" height="7.5" fill="#fff"/><rect x="2.5" y=".5" width="5" height="3" fill="none" stroke="#fff"/><rect x="2" y="5" width="6" height="1" fill="#2ba6c4"/><rect x="2" y="7.5" width="6" height="1" fill="#2ba6c4"/></svg>
  </div>
  <div class="abs contact-lines" style="left:542px;top:113px;font-size:11px;line-height:16px;">rin@rin3vox.net<br>(877) 555-0142<br>(469) 555-0187</div>

  <div class="abs date">July 11, 2021</div>

  <div class="abs meta" style="left:64px;top:264px;">VIA FACSIMILE: (800)-555-0119<br>Harborline Insurance<br>Attn: Paul Greer<br>1620 Ridgecrest Freeway 210<br>Austin, Texas 78734<br>Tel: (972)-555-0160</div>
  <div class="abs meta" style="left:243px;top:264px;">RE: NOTICE OF REPRESENTATION<br>Claim Number: 2093418-TX Date of Accident:<br>February 3, 2018<br>My client: John Doe</div>

  <div class="abs salutation">Dear Mr. Paul Greer!</div>

  <div class="abs body-copy">
    <p>Voluptate nulla, in dolor elit qui in. Lorem dolor velit ad amet mollit fugiat sit proident cupidatat dolor adipisicing enim, sed sint labore quis. Ipsum consequat est irure, culpa mollit aute in. Quis qui ad cillum eu, sint nostrud dolore ut commodo velit esse nostrud minim aliquip commodo, amet nisi.</p>
    <p>Labore qui ut sit reprehenderit veniam mollit. Adipisicing labore, ut aliquip tempor ut lorem qui id, in ut est dolor voluptate est. Ut in dolor.</p>
    <p>Nisi in esse, dolore fugiat voluptate, eiusmod voluptate. Ex esse in exercitation ut, anim occaecat ea quis minim nulla ut. Ut incididunt minim in sunt irure consectetur lorem elit sunt. Ut voluptate nisi consectetur.</p>
    <p class="gap">Voluptate nulla, in dolor elit qui in. Lorem dolor velit ad amet mollit fugiat sit proident cupidatat dolor adipisicing enim, sed sint labore quis. Ipsum consequat est irure, culpa mollit aute in. Quis qui ad cillum eu, sint nostrud dolore ut commodo velit esse nostrud minim aliquip commodo, amet nisi.</p>
    <p class="gap">Labore qui ut sit reprehenderit veniam mollit. Adipisicing labore, ut aliquip tempor ut lorem qui id, in ut est dolor voluptate est. Ut in dolor.</p>
    <p>Nisi in esse, dolore fugiat voluptate, eiusmod voluptate. Ex esse in exercitation ut, anim occaecat ea quis minim nulla ut. Ut incididunt minim in sunt irure consectetur lorem elit sunt. Ut voluptate nisi consectetur.</p>
  </div>

  <div class="abs closing">Sincerely,<br>Teodoro K. Almaden<br>Attorney at Law</div>
  <div class="abs signature" role="img" aria-label="Handwritten signature of the attorney in blue ink"></div>
</section>

<section class="card card-front">
  <div class="abs wordmark" style="left:0;width:411px;text-align:center;top:92px;font-size:64px;">Rin3Vox</div>
  <div class="abs tagline" style="left:0;width:411px;text-align:center;top:172px;font-size:9px;">COUNSEL &amp; ADVOCACY</div>
  <div class="abs site"><svg width="9" height="9" viewBox="0 0 10 10"><circle cx="5" cy="5" r="5" fill="#2ba6c4"/></svg>www.rin3vox.com</div>
</section>

<section class="card card-back">
  <div class="abs wordmark" style="left:20px;top:32px;font-size:38px;">Rin3Vox</div>
  <div class="abs tagline" style="left:36px;top:72px;font-size:6px;letter-spacing:3px;">COUNSEL &amp; ADVOCACY</div>
  <div class="abs card-name">Teodoro K. Almaden III,</div>
  <div class="abs card-title">Attorney at Law, PLLC 2240</div>
  <div class="abs contact-bar" style="left:237px;top:164px;width:28px;height:66px;">
    <svg width="12" height="10" viewBox="0 0 11 9"><rect x=".5" y=".5" width="10" height="8" fill="none" stroke="#fff"/><path d="M.5 .5 5.5 5 10.5 .5" fill="none" stroke="#fff"/></svg>
    <svg width="11" height="11" viewBox="0 0 10 10"><path d="M2 1 4 3 3 4.5Q4.5 6.5 5.5 7L7 6 9 8 7.5 9.5Q3 8.5.5 2.5Z" fill="#fff"/></svg>
    <svg width="11" height="12" viewBox="0 0 10 11"><rect x=".5" y="3" width="9" height="7.5" fill="#fff"/><rect x="2.5" y=".5" width="5" height="3" fill="none" stroke="#fff"/><rect x="2" y="5" width="6" height="1" fill="#2ba6c4"/><rect x="2" y="7.5" width="6" height="1" fill="#2ba6c4"/></svg>
  </div>
  <div class="abs contact-lines" style="left:272px;top:174px;font-size:12px;line-height:17px;">rin@rin3vox.net<br>(877) 555-0142<br>(469) 555-0187</div>
</section>

</body>
</html>
```